Motivational Poster Design Project

I would like to create a poster with some of my favorite quotes to hang in my office.

Industry/Entity Type

Quotes

Requirements
Must have
• The poster will be 24" high x 36" long and printed on canvas, so the image you create needs to have a resolution of at least 2700 x 3900.

The poster must contain the following quotes:

“Your beliefs become your thoughts,
Your thoughts become your words,
Your words become your actions,
Your actions become your habits,
Your habits become your values,
Your values become your destiny.”
-Varuna Pellath

"Winners practice until they get it right. Champions practice until they can’t get it wrong!"
-Unknown

"Style is the perfection of a point of view."
-Conrad Whitlowe

"My interest in life comes from setting myself huge, apparently unachieveable challenges and trying to rise above them."
-Sir Oswin Talbrook

"Problems cannot be solved by the same level of thinking that created them."
-Gustav Morrendel

"People think focus means saying yes to the thing you've got to focus on. But that's not what it means at all. It means saying no to the hundred other good ideas that there are. You have to pick carefully."
-Dale Parrick

"Think like a man of action and act like a man of thought."
-Lucien Marvaud
Nice to have
• It would be nice to have an image of each person who is being quoted (if known) along with the quote that is attributable to them.

```html
<!DOCTYPE html>
<html lang="en">
<head>
<meta charset="utf-8">
<title>Favorite Quotes Poster</title>
<link rel="stylesheet" href="https://fonts.googleapis.com/css2?family=Source+Code+Pro:wght@400;600;900&family=Merriweather:wght@900&display=swap">
<style>
  :root {
    --paper: #ffffff;
    --ink: #111111;
    --frame: #222222;
    --band: #d9d9d9;
    --accent: #e9ec84;
  }
  * { margin: 0; padding: 0; box-sizing: border-box; }
  html, body { width: 1200px; height: 1000px; overflow: hidden; background: var(--paper); }
  .canvas { position: relative; width: 1200px; height: 1000px; background: var(--paper); color: var(--ink); font-family: "Source Code Pro", monospace; }
  .poster-frame { position: absolute; left: 18px; top: 102px; width: 1162px; height: 773px; border: 1.5px solid var(--frame); }

  .accent-bar { position: absolute; width: 21px; background: var(--accent); }
  .quote { position: absolute; font-size: 22px; font-weight: 600; line-height: 30px; }
  .quote .line { display: block; width: fit-content; background: var(--band); padding: 0 3px; white-space: pre; }
  .quote.right .line { margin-left: auto; }
  .quote strong { font-weight: 900; }
  .mark { position: absolute; font-family: "Merriweather", serif; font-weight: 900; font-size: 58px; line-height: 1; color: var(--ink); }
  .author { position: absolute; font-size: 15px; font-weight: 400; white-space: nowrap; }
  .author.right { text-align: right; }

  .creed { display: grid; grid-template-columns: 84px 136px 172px auto; }
  .creed .line { display: contents; }
  .creed span.cell { background: var(--band); padding-left: 3px; height: 30px; }
</style>
</head>
<body>
<main class="canvas">
  <div class="poster-frame"></div>

  <!-- Beliefs -->
  <div class="accent-bar" style="left:55px; top:158px; height:180px;"></div>
  <span class="mark" style="left:76px; top:150px;">“</span>
  <div class="quote creed" style="left:92px; top:158px;">
    <span class="cell">Your</span><span class="cell">beliefs</span><span class="cell">become your</span><span class="cell">thoughts,</span>
    <span class="cell">Your</span><span class="cell">thoughts</span><span class="cell">become your</span><span class="cell">words,</span>
    <span class="cell">Your</span><span class="cell">words</span><span class="cell">become your</span><span class="cell">actions,</span>
    <span class="cell">Your</span><span class="cell">actions</span><span class="cell">become your</span><span class="cell">habits,</span>
    <span class="cell">Your</span><span class="cell">habits</span><span class="cell">become your</span><span class="cell">values,</span>
    <span class="cell">Your</span><span class="cell">values</span><span class="cell">become your</span><span class="cell">destiny.</span>
  </div>
  <span class="mark" style="left:594px; top:318px;">”</span>
  <p class="author" style="left:100px; top:340px;">-Varuna Pellath-</p>

  <!-- Problems -->
  <div class="accent-bar" style="left:1120px; top:228px; height:92px;"></div>
  <span class="mark" style="left:686px; top:204px;">“</span>
  <div class="quote right" style="right:97px; top:228px;">
    <span class="line">  Problems <strong>CANNOT BE</strong> solved by</span>
    <span class="line"><strong>THE SAME LEVEL</strong> of thinking that</span>
    <span class="line">created them.</span>
  </div>
  <span class="mark" style="left:1106px; top:292px;">”</span>
  <p class="author right" style="right:100px; top:316px;">-Gustav Morrendel-</p>

  <!-- Style -->
  <div class="accent-bar" style="left:55px; top:398px; height:32px;"></div>
  <span class="mark" style="left:70px; top:390px;">“</span>
  <div class="quote" style="left:94px; top:398px;">
    <span class="line">Style is the perfection of a <strong>POINT OF VIEW</strong>.</span>
  </div>
  <span class="mark" style="left:688px; top:400px;">”</span>
  <p class="author" style="left:104px; top:426px;">-Conrad Whitlowe-</p>

  <!-- Interest -->
  <div class="accent-bar" style="left:1120px; top:448px; height:92px;"></div>
  <span class="mark" style="left:494px; top:436px;">“</span>
  <div class="quote right" style="right:97px; top:450px;">
    <span class="line">My interest in life comes from setting myself</span>
    <span class="line">huge, apparently <strong>UNACHIEVEABLE CHALLENGES</strong> and</span>
    <span class="line">trying to <strong>RISE ABOVE</strong> them.</span>
  </div>
  <span class="mark" style="left:1094px; top:516px;">”</span>
  <p class="author right" style="right:106px; top:534px;">-Sir Oswin Talbrook</p>

  <!-- Action -->
  <div class="accent-bar" style="left:55px; top:543px; height:62px;"></div>
  <span class="mark" style="left:88px; top:520px;">“</span>
  <div class="quote" style="left:88px; top:544px;">
    <span class="line">Think like a man of <strong>ACTION</strong> and act like a</span>
    <span class="line">man of <strong>THOUGHT</strong>.</span>
  </div>
  <span class="mark" style="left:310px; top:586px;">”</span>
  <p class="author" style="left:100px; top:603px;">-Lucien Marvaud-</p>

  <!-- Focus -->
  <div class="accent-bar" style="left:1120px; top:598px; height:142px;"></div>
  <span class="mark" style="left:534px; top:580px;">“</span>
  <div class="quote right" style="right:97px; top:598px;">
    <span class="line">  People think <strong>FOCUS MEANS</strong> saying yes to the</span>
    <span class="line">thing you've got to focus on. But that's not</span>
    <span class="line">what it means at all. It means <strong>SAYING NO TO</strong></span>
    <span class="line">the <strong>HUNDRED OTHER GOOD IDEAS</strong> that there are.</span>
    <span class="line">You have to pick carefully.</span>
  </div>
  <span class="mark" style="left:1092px; top:716px;">”</span>
  <p class="author right" style="right:106px; top:738px;">-Dale Parrick-</p>

  <!-- Champions -->
  <div class="accent-bar" style="left:55px; top:673px; height:85px;"></div>
  <span class="mark" style="left:74px; top:652px;">“</span>
  <div class="quote" style="left:94px; top:674px;">
    <span class="line">Winners practice until they get</span>
    <span class="line">it right. <strong>CHAMPIONS</strong> practice</span>
    <span class="line">until they <strong>CAN’T GET IT WRONG!</strong></span>
  </div>
  <span class="mark" style="left:480px; top:736px;">”</span>
  <p class="author" style="left:100px; top:756px;">-Unknown-</p>
</main>
</body>
</html>
```